International non-profit org needs web design

A new non-profit global organization called The Worldwide Venture Bridge Council (WVC) needs a web design. The organization is a global community of professionals engaged in the commercialization aspects of innovation. The members of the community share experience and knowledge about exemplary practices and business models in order to continuoulsy improve the field of expertise.

Target Market(s)

governments, investors, universities, professionala

Industry/Entity Type

Non-Profit

Requirements
Must have
• landing page and capability to add tabs

```html
<!DOCTYPE html>
<html lang="en">
<head>
<meta charset="utf-8">
<title>The Worldwide Venture Bridge Council</title>
<link href="https://fonts.googleapis.com/css2?family=PT+Sans+Narrow:wght@700&family=Ubuntu:wght@400;500&family=Open+Sans:wght@400;600&display=swap" rel="stylesheet">
<style>
:root{
  --red:#d71f26;
  --red-deep:#b3121a;
  --red-bright:#ee3a40;
  --ink:#2b2b2b;
  --muted:#555;
  --orange:#ff9a00;
  --orange-deep:#ff6e00;
  --nav:#1e1e1e;
  --band:#e3e3e3;
  --foot:#222;
  --foot-text:#777;
}
*{margin:0;padding:0;box-sizing:border-box}
html,body{width:1112px;height:1200px;overflow:hidden}
body{position:relative;font-family:"Open Sans",sans-serif;color:var(--ink);background:#fff}
.abs{position:absolute}
.header{left:0;top:0;width:1112px;height:97px;background:linear-gradient(#fff,#ececec)}
.brand{left:82px;top:24px;display:flex;align-items:center;gap:10px}
.brand-dot{width:42px;height:42px;border-radius:50%;background:var(--red)}
.brand-name{font-family:"Ubuntu",sans-serif;font-weight:500;font-size:46px;color:var(--red);line-height:1}
.brand-rule{width:1px;height:56px;background:#444;margin:0 4px}
.brand-sub{font-family:"Ubuntu",sans-serif;font-weight:500;font-size:11px;letter-spacing:1px;line-height:13px;color:#222}
.call{right:76px;top:30px;font-family:"PT Sans Narrow",sans-serif;font-size:26px;color:#444}
.call span{color:var(--red)}
.hero{left:0;top:97px;width:1112px;height:387px;background:radial-gradient(ellipse at 55% 40%,var(--red-bright),var(--red) 45%,var(--red-deep))}
.nav{left:80px;top:97px;width:953px;height:42px;background:linear-gradient(#333,#111);display:flex;box-shadow:0 3px 6px rgba(0,0,0,.4)}
.nav a{color:#fff;text-decoration:none;font-family:"Ubuntu",sans-serif;font-size:13.5px;display:flex;align-items:center;justify-content:center;border-right:1px solid #3a3a3a}
.nav a.on{background:#0d0d0d}
.slide-arrow{top:283px;width:28px;height:56px;background:#222;color:#fff;font-size:22px;display:flex;align-items:center;justify-content:center}
.slide-arrow.l{left:54px;border-radius:28px 0 0 28px}
.slide-arrow.r{left:1034px;border-radius:0 28px 28px 0}
.hero-title{left:143px;top:198px;font-family:"PT Sans Narrow",sans-serif;font-size:40px;color:#fff;letter-spacing:-.5px}
.hero-text{left:144px;top:255px;width:410px;font-size:12.5px;line-height:17px;color:#fff}
.btn{background:linear-gradient(var(--orange),var(--orange-deep));color:#fff;font-family:"Ubuntu",sans-serif;font-weight:500;display:flex;align-items:center;justify-content:center;border-radius:3px}
.readmore{left:143px;top:331px;width:146px;height:38px;font-size:17px}
.chart{left:590px;top:190px}
.dots{left:520px;top:442px;display:flex;gap:5px}
.dots i{width:14px;height:14px;border-radius:50%;background:#7a0a0e;box-shadow:inset 0 1px 2px rgba(0,0,0,.6)}
.dots i:first-child{background:#333}
.features{left:0;top:484px;width:1112px;height:150px;background:linear-gradient(#fafafa,#f0f0f0)}
.feature{top:516px;display:flex;gap:14px}
.feature-icon{width:58px;height:58px;border-radius:4px}
.feature h3{font-family:"Ubuntu",sans-serif;font-weight:400;font-size:20px;color:#222;margin-bottom:4px}
.feature p{font-size:11px;line-height:15.5px;color:#444;width:210px}
.divider{top:516px;width:2px;height:92px;background:linear-gradient(rgba(0,0,0,0),#ddd,rgba(0,0,0,0))}
.section-title{font-family:"Ubuntu",sans-serif;font-size:19px;color:#222}
.section-title span{color:var(--red)}
.avatar{left:87px;top:723px;width:68px;height:62px;border:3px solid #fff;box-shadow:0 0 3px #bbb;background:radial-gradient(#555,#2a2a2a)}
.quote{left:170px;top:731px;width:375px;font-size:11.5px;line-height:15.5px;color:#444}
.author{left:170px;top:782px;font-size:11.5px;font-weight:600;color:#222}
.author span{color:var(--red)}
.pager{left:171px;top:811px;width:86px;height:26px;border:1px solid #ccc;border-radius:3px;background:linear-gradient(#fff,#e6e6e6);display:flex}
.pager b{flex:1;display:flex;align-items:center;justify-content:center;font-size:10px}
.pager b:first-child{border-right:1px solid #ccc;color:var(--red)}
.badge{background:#e4e4e4;border-radius:4px}
.join-band{left:0;top:900px;width:1112px;height:86px;background:var(--band)}
.join-text{left:80px;top:930px;font-family:"Ubuntu",sans-serif;font-size:22px;color:#333}
.join{left:884px;top:925px;width:146px;height:39px;font-size:17px}
.footer{left:0;top:986px;width:1112px;height:214px;background:linear-gradient(#333,var(--foot))}
.foot-links{left:82px;top:1023px;display:flex;gap:8px;color:#fff;font-family:"Ubuntu",sans-serif;font-size:13.5px}
.foot-small{font-size:10.5px;line-height:14px;color:var(--foot-text)}
.foot-head{font-family:"Ubuntu",sans-serif;font-size:13.5px;color:#fff}
.social{top:1093px;width:24px;height:24px;border-radius:4px}
.field{left:797px;width:233px;height:32px;border:1px solid #4a4a4a;background:#262626;font-size:10.5px;color:#666;padding:9px 11px}
.send{left:948px;top:1134px;width:82px;height:26px;font-size:13px}
</style>
</head>
<body>
<header class="abs header"></header>
<div class="abs brand">
  <div class="brand-dot"></div>
  <div class="brand-name">WVC</div>
  <div class="brand-rule"></div>
  <div class="brand-sub">WORLDWIDE<br>VENTURE BRIDGE<br>COUNCIL</div>
</div>
<div class="abs call"><span>Call Us</span>&nbsp; 416-555-0193</div>

<section class="abs hero"></section>
<nav class="abs nav">
  <a class="on" style="width:102px">Home</a>
  <a style="width:130px">About Us</a>
  <a style="width:108px">Ideas</a>
  <a style="width:232px">Venture Bridge Council</a>
  <a style="width:124px">Partners</a>
  <a style="width:127px">Members</a>
  <a style="width:130px;border:0">Contact Us</a>
</nav>
<div class="abs slide-arrow l">&#10094;</div>
<div class="abs slide-arrow r">&#10095;</div>
<h1 class="abs hero-title">Many visitors every month</h1>
<p class="abs hero-text">Lorem ipsum dolor sit amet, consectetur adipisicing elit, sed do eiusmod tempor incididunt ut labore et dolore magna aliqua. Ut enim ad minim veniam, quis nostrud exercitation ullamco laboris nisi</p>
<div class="abs btn readmore">Readmore</div>
<svg class="abs chart" width="390" height="185" viewBox="0 0 390 185">
  <polygon points="4,172 56,108 143,89 223,65 297,21 379,4 379,175 4,175" fill="#fff" fill-opacity=".16"/>
  <polyline points="4,172 56,108 143,89 223,65 297,21 379,4" fill="none" stroke="#fff" stroke-width="1.5"/>
  <g fill="#fff"><circle cx="4" cy="172" r="4.5"/><circle cx="56" cy="108" r="4.5"/><circle cx="143" cy="89" r="4.5"/><circle cx="223" cy="65" r="4.5"/><circle cx="297" cy="21" r="4.5"/></g>
</svg>
<div class="abs dots"><i></i><i></i><i></i></div>

<section class="abs features"></section>
<div class="abs feature" style="left:80px">
  <div class="feature-icon" role="img" aria-label="Person silhouette icon" style="background:linear-gradient(#444,#111);border-radius:30px 30px 4px 4px"></div>
  <div><h3>The Mission</h3><p>Facilitate improvement of Policies, Practices, Models and&nbsp; Evidence-based success measurements</p></div>
</div>
<div class="abs divider" style="left:385px"></div>
<div class="abs feature" style="left:406px">
  <div class="feature-icon" role="img" aria-label="Document icon" style="background:linear-gradient(#fafafa,#cfd4d8);border:1px solid #ccc"></div>
  <div><h3>Objectives</h3><p>Share exemplary practices in the commercialization of research outcomes in our countries and regions</p></div>
</div>
<div class="abs divider" style="left:703px"></div>
<div class="abs feature" style="left:731px">
  <div class="feature-icon" role="img" aria-label="Parcel box icon" style="background:linear-gradient(#e8c17a,#c08f3f)"></div>
  <div><h3>Value Proposition</h3><p>Greater visibility in real time on new approaches to commercialization</p></div>
</div>

<h2 class="abs section-title" style="left:88px;top:678px"><span>Member</span> Testimonials</h2>
<div class="abs avatar" role="img" aria-label="Member portrait"></div>
<p class="abs quote">&ldquo;&nbsp; Lorem ipsum dolor sit amet, consectetur adipisicing elit, sed do eiusmod tempor incididunt ut labore et dolore magna aliqua. Ut enim ad minim veniam, quis nostrud exercitation ullamco laboris nisi &rdquo;</p>
<div class="abs author"><span>Daniel Hersey</span> - Toronto</div>
<div class="abs pager"><b>&#9664;</b><b>&#9654;</b></div>

<h2 class="abs section-title" style="left:572px;top:678px">Thank&rsquo;s to</h2>
<div class="abs badge" style="left:576px;top:716px;width:180px;height:52px"></div>
<div class="abs badge" style="left:796px;top:722px;width:102px;height:38px"></div>
<div class="abs badge" style="left:580px;top:794px;width:216px;height:32px"></div>
<div class="abs badge" style="left:812px;top:794px;width:186px;height:32px"></div>

<section class="abs join-band"></section>
<div class="abs join-text">48 members &ndash; 18 countries, We need more bright people like you</div>
<div class="abs btn join">Join Now</div>

<footer class="abs footer"></footer>
<div class="abs foot-links">About Us <span>&bull;</span> Privacy Policy <span>&bull;</span> Help <span>&bull;</span> Blog</div>
<div class="abs foot-small" style="left:81px;top:1050px">Copyright &copy; 2011 WVC The Worldwide Venture Bridge Council<br>Use of this website constitutes acceptance User Agreement</div>
<div class="abs social" style="left:81px;background:#4fb6e8"></div>
<div class="abs social" style="left:115px;background:#3b5a9a"></div>
<div class="abs social" style="left:148px;background:#f08a1c"></div>
<div class="abs foot-head" style="left:423px;top:1023px">Dr. Lena Marsh</div>
<div class="abs foot-small" style="left:422px;top:1050px">The Horizontal Policy Roundtable Harbour Conference Hall,<br>September 29, 2011</div>
<div class="abs foot-small" style="left:422px;top:1092px;color:#ddd">lena.marsh@venturebridge.org &nbsp; - &nbsp; Cell: 416-555-0193</div>
<div class="abs foot-head" style="left:799px;top:1023px">Contact Us</div>
<div class="abs field" style="top:1050px">Username</div>
<div class="abs field" style="top:1089px">Email</div>
<div class="abs btn send">Send</div>
</body>
</html>
```